church business card design

we have a logo and would like our business card to complement the logo. we would prefer the logo in white on a coloured background - probably blue. Under the logo or near it we would have the Words 'Love God. Love people. Follow Jesus.'
We would like some yellow/gold highlights. We like the design by mintaro quill 4821 front of card - https://www.pelvarostudio.com/businesscard-design/contest/5812094

Our church is multicultural, inner city, friendly, warm welcoming and that's the feel we would like. there's also an element of being spontaneous, so a swirl or swoosh might help give that feel. the example card above had some curved shapes on the front of the card for example.
on the second side of the card would have the details of the Senior Pastor and the contact details for the church.
after the business card we would be looking at letterhead and an A5 flyer for printing but also as document templates so we can create invitations etc going forward

```html
<!DOCTYPE html>
<html lang="en">
<head>
<meta charset="utf-8">
<title>Cornerway Church – Business Card</title>
<link href="https://fonts.googleapis.com/css2?family=Exo+2:wght@400;500;600;700&display=swap" rel="stylesheet">
<style>
  :root {
    --backdrop: #2b2b2d;
    --card-white: #ffffff;
    --brand-blue: #3438c4;
    --deep-blue: #1c2078;
    --gold: #e2b13c;
    --gold-soft: #f1cf72;
    --ink: #111111;
    --rule: #8a8a8a;
    --white: #ffffff;
  }
  * { box-sizing: border-box; margin: 0; padding: 0; }
  html, body {
    width: 1200px; height: 1108px; overflow: hidden;
    background: var(--backdrop);
    font-family: "Exo 2", "Segoe UI", sans-serif;
  }
  .sheet {
    position: relative; width: 1200px; height: 1108px;
    display: flex; justify-content: center; align-items: center; gap: 60px;
  }
  .card {
    width: 420px; height: 680px; border-radius: 26px;
    position: relative; overflow: hidden;
  }
  .swoosh { position: absolute; left: 0; width: 100%; pointer-events: none; }

  /* front */
  .card-front { background: var(--card-white); color: var(--ink); text-align: center; }
  .brand { position: absolute; top: 86px; left: 0; right: 0; }
  .brand-name {
    font-size: 58px; font-weight: 700; color: var(--brand-blue);
    letter-spacing: 1px; line-height: 1;
  }
  .brand-sub {
    margin-top: 14px; font-size: 20px; font-weight: 700; color: var(--brand-blue);
    letter-spacing: 26px; padding-left: 26px;
  }
  .brand-accent { width: 70px; height: 3px; background: var(--gold); margin: 16px auto 0; border-radius: 2px; }
  .person { position: absolute; top: 290px; left: 0; right: 0; }
  .person-name { font-size: 30px; font-weight: 700; color: var(--brand-blue); letter-spacing: 0.5px; }
  .person-role { font-size: 20px; font-weight: 500; margin-top: 2px; }
  .icon-row {
    position: absolute; top: 372px; left: 40px; right: 40px;
    display: flex; align-items: center; gap: 10px;
  }
  .icon-row .rule { flex: 1; height: 1px; background: var(--rule); }
  .icon {
    width: 34px; height: 34px; border-radius: 5px; background: var(--brand-blue);
    display: flex; align-items: center; justify-content: center;
    box-shadow: inset 0 -3px 0 var(--gold);
  }
  .contact { position: absolute; top: 428px; left: 0; right: 0; font-size: 20px; line-height: 1.3; font-weight: 500; }
  .contact .phone { font-size: 24px; font-weight: 600; }
  .contact .web-accent { color: var(--brand-blue); }
  .divider { width: 300px; height: 1px; background: var(--rule); margin: 10px auto; }
  .address { font-size: 20px; font-weight: 500; line-height: 1.3; }
  .card-front .swoosh { bottom: 0; height: 80px; }

  /* back */
  .card-back {
    background: linear-gradient(160deg, var(--brand-blue) 0%, #2a2ea3 50%, var(--deep-blue) 100%);
    color: var(--white); text-align: center;
  }
  .card-back .swoosh-top { top: 0; height: 240px; }
  .card-back .swoosh-bottom { bottom: 0; height: 260px; }
  .back-brand { position: absolute; top: 270px; left: 0; right: 0; }
  .back-mark { font-size: 50px; font-weight: 700; letter-spacing: 1px; line-height: 1; color: var(--white); }
  .back-sub {
    margin-top: 14px; font-size: 18px; font-weight: 700; color: var(--gold-soft);
    letter-spacing: 22px; padding-left: 22px;
  }
  .back-tagline {
    position: absolute; top: 400px; left: 0; right: 0;
    font-size: 22px; font-weight: 600; color: var(--white);
  }
  .back-tagline .dot { color: var(--gold); }
</style>
</head>
<body>
<main class="sheet">
  <section class="card card-front" aria-label="Card front">
    <div class="brand">
      <div class="brand-name">Cornerway</div>
      <div class="brand-sub">CHURCH</div>
      <div class="brand-accent"></div>
    </div>
    <div class="person">
      <div class="person-name">DANIEL MERCER</div>
      <div class="person-role">Managing Director</div>
    </div>
    <div class="icon-row">
      <span class="rule"></span>
      <span class="icon" aria-label="Phone">
        <svg width="20" height="20" viewBox="0 0 24 24" fill="#fff"><path d="M6.6 10.8a15 15 0 0 0 6.6 6.6l2.2-2.2a1 1 0 0 1 1-.25 11.4 11.4 0 0 0 3.6.57 1 1 0 0 1 1 1V20a1 1 0 0 1-1 1A17 17 0 0 1 3 4a1 1 0 0 1 1-1h3.5a1 1 0 0 1 1 1c0 1.25.2 2.45.57 3.57a1 1 0 0 1-.25 1z"/></svg>
      </span>
      <span class="icon" aria-label="Email">
        <svg width="20" height="16" viewBox="0 0 24 18" fill="none" stroke="#fff" stroke-width="2"><rect x="1" y="1" width="22" height="16" rx="1"/><path d="M1 1l11 9 11-9"/></svg>
      </span>
      <span class="icon" aria-label="Website">
        <svg width="20" height="20" viewBox="0 0 24 24" fill="none" stroke="#fff" stroke-width="1.8"><circle cx="12" cy="12" r="10"/><path d="M2 12h20M12 2c3 3 3 17 0 20M12 2c-3 3-3 17 0 20"/></svg>
      </span>
      <span class="rule"></span>
    </div>
    <div class="contact">
      <div class="phone">044-987 210 346</div>
      <div>hello@cornerwaychurch.org</div>
      <div>www.<span class="web-accent">cornerwaychurch</span>.org</div>
      <div class="divider"></div>
      <div class="address">18, Harrow Lane<br>30417, Eastvale</div>
    </div>
    <svg class="swoosh" viewBox="0 0 420 80" preserveAspectRatio="none" aria-hidden="true">
      <path d="M0 50 C120 10 260 70 420 24 L420 80 L0 80 Z" fill="var(--brand-blue)"/>
      <path d="M0 42 C120 2 260 62 420 16" fill="none" stroke="var(--gold)" stroke-width="4"/>
    </svg>
  </section>

  <section class="card card-back" aria-label="Card back">
    <svg class="swoosh swoosh-top" viewBox="0 0 420 240" preserveAspectRatio="none" aria-hidden="true">
      <path d="M0 120 C110 40 250 200 420 70 L420 0 L0 0 Z" fill="#ffffff" opacity="0.07"/>
      <path d="M0 150 C120 60 240 210 420 100" fill="none" stroke="var(--gold)" stroke-width="3" opacity="0.9"/>
      <path d="M0 170 C130 90 250 230 420 130" fill="none" stroke="#ffffff" stroke-width="1.5" opacity="0.35"/>
    </svg>
    <div class="back-brand">
      <div class="back-mark">CORNERWAY</div>
      <div class="back-sub">CHURCH</div>
    </div>
    <div class="back-tagline">Love God<span class="dot">.</span> Love People<span class="dot">.</span> Follow Jesus<span class="dot">.</span></div>
    <svg class="swoosh swoosh-bottom" viewBox="0 0 420 260" preserveAspectRatio="none" aria-hidden="true">
      <path d="M0 150 C140 60 280 230 420 110 L420 260 L0 260 Z" fill="#ffffff" opacity="0.07"/>
      <path d="M0 130 C140 40 280 210 420 90" fill="none" stroke="#ffffff" stroke-width="1.5" opacity="0.35"/>
      <path d="M0 160 C150 70 270 240 420 130" fill="none" stroke="var(--gold)" stroke-width="4"/>
      <path d="M0 210 C160 150 280 260 420 200 L420 260 L0 260 Z" fill="var(--deep-blue)" opacity="0.6"/>
    </svg>
  </section>
</main>
</body>
</html>
```